Thornwell Building Company - advertisement poster

I am looking to print some canvas signs to advertise my general contracting company, Thornwell Building Company. The sign will measure 6' long x 3' high so the size should match that ratio. I already have a logo icon, which is the Letter 'A' and some trees that I would like to incorporate, see attached. I would also like the to have the following information listed:
1) phone number: 472-318-6095
2) email: thornwellbuildingcompany@mailvistra.net
3) website: thornwellbuildingcompany.com
4) Lic#5386204
5) I want to use this text: "BUILD WITH THE T-CREW!"

The ad should be relatively simple and clean. Black and Green are my company colors. I am open to creative ideas!

Target Market(s)

People looking to renovate their homes

Industry/Entity Type

Construction

Colors
59FF00
82FF00
B8FF75
E3FFCB
F4FFEA

Requirements
Must have
• Must have my company logo
Should not have
• No photos or complex graphics

```html
<!DOCTYPE html>
<html lang="en">
<head>
<meta charset="utf-8">
<title>Thornwell Building Company – Canvas Sign</title>
<link rel="stylesheet" href="https://fonts.googleapis.com/css2?family=Fira+Sans:wght@500;700;800&family=Oswald:wght@600&display=swap">
<style>
  :root {
    --page: #a9a9a9;
    --navy: #0d1b5c;
    --navy-deep: #081344;
    --green: #6cb843;
    --black: #050505;
    --white: #ffffff;
    --warm: #c98a3a;
    --stone: #8c8f9c;
  }
  html, body {
    margin: 0;
    width: 1000px;
    height: 1200px;
    overflow: hidden;
    background: var(--page);
  }
  .sign {
    position: absolute;
    left: 50px;
    top: 375px;
    width: 900px;
    height: 450px;
    overflow: hidden;
    background: linear-gradient(135deg, var(--navy-deep), var(--navy));
    font-family: "Fira Sans", Arial, sans-serif;
  }
  .house-photo {
    position: absolute;
    left: 400px;
    top: 0;
    width: 500px;
    height: 450px;
    background:
      linear-gradient(180deg, var(--navy) 0%, rgba(13,27,92,0) 22%),
      linear-gradient(100deg, #f1e6cf 0%, var(--warm) 30%, #e9e4da 45%, var(--stone) 60%, #f3e9c8 80%, #d8d2c4 100%);
  }
  .brand {
    position: absolute;
    left: 0;
    top: 0;
    width: 400px;
    height: 232px;
    display: flex;
    flex-direction: column;
    align-items: center;
    justify-content: center;
    gap: 14px;
  }
  .brand-mark {
    width: 54px;
    height: 54px;
    border-radius: 50%;
    background: var(--green);
  }
  .brand-name {
    margin: 0;
    color: var(--white);
    font-weight: 700;
    font-size: 34px;
    line-height: 1.05;
    letter-spacing: 2px;
    text-align: center;
    text-transform: uppercase;
  }
  .slogan-band {
    position: absolute;
    left: 0;
    top: 231px;
    width: 419px;
    height: 124px;
    background: var(--green);
  }
  .slogan {
    position: absolute;
    left: 51px;
    top: 241px;
    margin: 0;
    color: var(--white);
    font-weight: 800;
    font-size: 46px;
    line-height: 48px;
    letter-spacing: -0.5px;
    text-shadow: 1px 2px 3px rgba(0,0,0,0.35);
  }
  .contact-band {
    position: absolute;
    left: 0;
    top: 355px;
    width: 394px;
    height: 95px;
    background: var(--black);
  }
  .contact-list {
    position: absolute;
    left: 51px;
    top: 375px;
    margin: 0;
    padding: 0;
    list-style: none;
    color: var(--white);
    font-weight: 500;
    font-size: 14.5px;
  }
  .contact-list li {
    display: flex;
    align-items: center;
    gap: 11px;
    height: 26px;
  }
  .contact-icon {
    width: 17px;
    height: 17px;
  }
  .phone-slab {
    position: absolute;
    left: 0;
    top: 0;
  }
  .phone {
    position: absolute;
    left: 590px;
    top: 363px;
    display: flex;
    align-items: center;
    gap: 8px;
  }
  .phone-number {
    color: var(--white);
    font-family: "Oswald", "Arial Narrow", sans-serif;
    font-weight: 600;
    font-size: 46px;
    line-height: 1;
  }
  .license {
    position: absolute;
    left: 627px;
    top: 414px;
    color: var(--green);
    font-weight: 500;
    font-size: 14px;
  }
</style>
</head>
<body>
  <main class="sign">
    <div class="house-photo" role="img" aria-label="Photo of a modern two-storey house with warm lighting at dusk"></div>

    <header class="brand">
      <span class="brand-mark"></span>
      <h1 class="brand-name">Thornwell<br>Building Company</h1>
    </header>

    <div class="slogan-band"></div>
    <h2 class="slogan">BUILD WITH<br>THE T-CREW!</h2>

    <div class="contact-band"></div>
    <ul class="contact-list">
      <li>
        <svg class="contact-icon" viewBox="0 0 20 20" aria-hidden="true">
          <circle cx="10" cy="10" r="10" fill="var(--green)"/>
          <g fill="none" stroke="#1a1a1a" stroke-width="1">
            <circle cx="10" cy="10" r="5"/>
            <ellipse cx="10" cy="10" rx="2.2" ry="5"/>
            <line x1="5" y1="10" x2="15" y2="10"/>
          </g>
        </svg>
        thornwellbuildingcompany.com
      </li>
      <li>
        <svg class="contact-icon" viewBox="0 0 20 20" aria-hidden="true">
          <circle cx="10" cy="10" r="10" fill="var(--green)"/>
          <g fill="none" stroke="#1a1a1a" stroke-width="1">
            <rect x="5" y="6.5" width="10" height="7"/>
            <polyline points="5,6.5 10,10.5 15,6.5"/>
          </g>
        </svg>
        thornwellbuildingcompany@mailvistra.net
      </li>
    </ul>

    <svg class="phone-slab" width="900" height="450" viewBox="0 0 900 450" aria-hidden="true">
      <polygon points="533,450 587,356 900,324 900,450" fill="var(--black)"/>
    </svg>
    <div class="phone">
      <svg width="26" height="42" viewBox="0 0 26 42" aria-hidden="true">
        <path d="M6 2 L12 1 L14 10 L10 13 C9 20 11 27 15 32 L19 30 L25 36 L21 41 C10 41 1 25 2 12 Z" fill="var(--green)"/>
      </svg>
      <span class="phone-number">472-318-6095</span>
    </div>
    <span class="license">Lic#5386204</span>
  </main>
</body>
</html>
```